We need a logo for our business which is a dental clinic (i.e. dentistry).
We would lilke designs using the colour blue, green and black incorporating the words Corvasta Dental, possibly a smile or a tooth image can be considered for incorporation in the logo.

Industry/Entity Type

Dental

```html
<!DOCTYPE html>
<html lang="en">
<head>
<meta charset="utf-8">
<title>Corvasta Dental – Business Cards</title>
<link href="https://fonts.googleapis.com/css2?family=Josefin+Sans:wght@400;600&display=swap" rel="stylesheet">
<style>
  :root {
    --bg: #e9e7e3;
    --card: #ffffff;
    --card-shade: #eeeeee;
    --teal: #1fb3d0;
    --teal-deep: #0f9bbd;
    --teal-light: #8fdcec;
    --green: #9ccc2f;
    --ink: #3a3a3a;
    --ink-soft: #555555;
  }
  * { margin: 0; padding: 0; box-sizing: border-box; }
  html, body { width: 1200px; height: 900px; overflow: hidden; }
  body {
    background: var(--bg);
    font-family: "Josefin Sans", Arial, sans-serif;
    display: flex;
    align-items: center;
    justify-content: center;
    gap: 60px;
  }
  .card {
    position: relative;
    width: 520px;
    height: 300px;
    border-radius: 30px;
    background: linear-gradient(160deg, var(--card) 0%, var(--card-shade) 100%);
    box-shadow: 0 10px 28px rgba(0,0,0,.18);
    overflow: hidden;
  }
  .brand {
    position: absolute;
    display: flex;
    align-items: center;
    gap: 10px;
  }
  .brand-dot {
    width: 30px; height: 30px;
    border-radius: 50%;
    background: var(--green);
  }
  .brand-name {
    font-weight: 600;
    font-size: 30px;
    color: var(--teal);
    line-height: 1;
    white-space: nowrap;
  }
  .front .brand { left: 190px; top: 42px; }
  .back .brand { left: 120px; top: 110px; }
  .back .brand-name { font-size: 36px; }
  .back .brand-dot { width: 36px; height: 36px; }

  .person {
    position: absolute;
    left: 40px;
    top: 128px;
    width: 190px;
    text-align: right;
    color: var(--ink);
    font-variant: small-caps;
    letter-spacing: 1.5px;
  }
  .person-name { font-size: 19px; font-weight: 600; }
  .person-role { font-size: 14px; margin-top: 2px; color: var(--ink-soft); }
  .person-address { font-size: 13px; margin-top: 10px; line-height: 1.35; color: var(--ink-soft); }

  .contacts {
    position: absolute;
    left: 250px;
    top: 128px;
    list-style: none;
    color: var(--ink-soft);
    font-size: 13px;
    letter-spacing: 1.2px;
    font-variant: small-caps;
  }
  .contacts li { display: flex; align-items: center; gap: 7px; height: 20px; }
  .contacts svg { width: 13px; height: 13px; flex: none; }
  .contacts .gap { margin-top: 4px; }

  .wave { position: absolute; left: 0; bottom: 0; width: 520px; height: 150px; }
</style>
</head>
<body>

<section class="card front">
  <div class="brand">
    <span class="brand-dot"></span>
    <span class="brand-name">Corvasta Dental</span>
  </div>

  <div class="person">
    <p class="person-name">Dana Whitlow</p>
    <p class="person-role">Owner : C.E.O</p>
    <p class="person-address">Suite # 118, Birch Court,<br>NY 10482</p>
  </div>

  <ul class="contacts">
    <li>
      <svg viewBox="0 0 14 14"><circle cx="7" cy="7" r="7" fill="#333"/><path d="M4.5 3.5l1.5 0 .6 2-1 .8a5 5 0 0 0 2.1 2.1l.8-1 2 .6 0 1.5c-3.5.3-6.3-2.5-6-6z" fill="#fff"/></svg>
      555-204-7731
    </li>
    <li>
      <svg viewBox="0 0 14 14"><circle cx="7" cy="7" r="7" fill="#333"/><rect x="4" y="5" width="6" height="5" fill="#fff"/><rect x="5" y="3" width="4" height="2.5" fill="#fff"/></svg>
      555-318-6642
    </li>
    <li>
      <svg viewBox="0 0 14 14"><circle cx="7" cy="7" r="7" fill="#333"/><rect x="5" y="3" width="4" height="8" rx="1" fill="#fff"/></svg>
      555-427-9015
    </li>
    <li class="gap">
      <svg viewBox="0 0 14 14"><circle cx="7" cy="7" r="7" fill="#333"/><rect x="3.5" y="4.5" width="7" height="5" fill="#fff"/><path d="M3.5 4.5l3.5 3 3.5-3" stroke="#333" stroke-width=".8" fill="none"/></svg>
      dana@corvastadental.com
    </li>
    <li>
      <svg viewBox="0 0 14 14"><circle cx="7" cy="7" r="7" fill="#333"/><circle cx="7" cy="7" r="3.6" fill="none" stroke="#fff" stroke-width=".9"/><path d="M3.4 7h7.2M7 3.4c-1.6 2.2-1.6 5 0 7.2M7 3.4c1.6 2.2 1.6 5 0 7.2" stroke="#fff" stroke-width=".7" fill="none"/></svg>
      www.corvastadental.com
    </li>
  </ul>

  <svg class="wave" viewBox="0 0 520 150" preserveAspectRatio="none" aria-hidden="true">
    <defs>
      <linearGradient id="teal-band" x1="0" y1="0" x2="1" y2="0">
        <stop offset="0" stop-color="var(--teal-deep)"/>
        <stop offset=".55" stop-color="var(--teal)"/>
        <stop offset="1" stop-color="var(--teal-light)"/>
      </linearGradient>
    </defs>
    <path d="M0 40 C 40 90, 180 120, 520 148 L 520 150 L 0 150 Z" fill="url(#teal-band)"/>
    <path d="M0 55 C 60 105, 220 128, 520 150 L 0 150 Z" fill="var(--teal-light)" opacity=".55"/>
    <path d="M0 22 C 40 70, 200 96, 520 138" fill="none" stroke="var(--green)" stroke-width="4"/>
  </svg>
</section>

<section class="card back">
  <div class="brand">
    <span class="brand-dot"></span>
    <span class="brand-name">Corvasta Dental</span>
  </div>
</section>

</body>
</html>
```